Powerpoint Design for business and consulting company - Brennig-Tautz

I am searching a design specialist who can help me to create a PowerPoint Design for my company. I'm in the business coaching and consulting industry.

The PPT master should be easy to use and include professional formatting (using the fonts of my website). In general, the slide master should have the look and feel of my website (in terms of fonts, colors, logos, possibility to place big photographs, having text and graph slides as well as photo slides with just 1 key message).

The PowerPoint design should fit my cooperate Identity (please see my website https://brennig-tautz.de).
My logos are attached.

Additional information:
- wide screen format - 16: 9
- right set up of a fitting color scheme
https: // tintrow. io / f6ded1-bfcbce-807f84-9cd3d1-666666
# 666666 (Dim Gray) - body / heading text
# 807F84 (Gray Web)
#BFCBCE (Silver Sand) - link hover
# 9cd3d1 (Powder Blue) - Link color
# F6DED1 (Champagne Pink)

- creation of chart templates, using chart tools, and different chart types etc.
- creation of different slide layouts to place content, pictures (in different sizes), optionally Media
- set up of display guide lines
- as well as standard elements, such as text boxes, lines, default shapes, etc.

• Powerpoint Design needs to have:
https://tintrow.io/f6ded1-bfcbce-807f84-9cd3d1-666666
# 807F84 (Gray Web)
# F6DED1 (Champagne Pink)

```html
<!DOCTYPE html>
<html lang="en">
<head>
<meta charset="utf-8">
<title>Brennig-Tautz – Presentation Master</title>
<link href="https://fonts.googleapis.com/css2?family=Varela+Round&family=Montserrat:wght@400;600&display=swap" rel="stylesheet">
<style>
:root{
  --dim:#666666;
  --gray:#807f84;
  --silver:#bfcbce;
  --blue:#9cd3d1;
  --pink:#f6ded1;
  --bg:#eceeef;
  --white:#ffffff;
  --ice:#e6f2f2;
}
*{box-sizing:border-box;margin:0;padding:0}
html,body{width:684px;height:1200px;overflow:hidden;background:var(--bg)}
body{position:relative;font-family:"Montserrat",sans-serif;color:var(--dim)}
.band{position:absolute;left:0;top:0}
.brand{position:absolute;top:26px;left:0;width:684px;text-align:center;font-family:"Varela Round",sans-serif;font-size:20px;color:var(--white);letter-spacing:.5px}
.hero{position:absolute;top:92px;width:300px;height:169px;font-size:14.63px}
.hero-left{left:30px}
.hero-right{left:354px}
.deck{position:absolute;left:22px;top:300px;display:grid;grid-template-columns:repeat(3,205px);column-gap:12px;row-gap:20px}
.slide{position:relative;width:20.5em;height:11.5em;background:var(--white);overflow:hidden;box-shadow:0 1px 3px rgba(0,0,0,.18);font-size:10px}
.hero .slide{font-size:inherit}
.photo{position:absolute}
.ph-warm{background:linear-gradient(135deg,#8b8a84 0%,#b59a86 40%,#d9734f 60%,#6c5f58 100%)}
.ph-mono{background:linear-gradient(120deg,#bdbdbd 0%,#8d8d8d 50%,#4f4f4f 100%)}
.ph-stairs{background:linear-gradient(160deg,#9fa39a 0%,#6e7468 45%,#c88a75 70%,#5b5756 100%)}
.ph-desk{background:linear-gradient(140deg,#c9c2b8 0%,#7e8a92 50%,#3e4a55 100%)}
.ph-soft{background:linear-gradient(150deg,#d9d4cc 0%,#b6ab9c 50%,#6f6a63 100%)}
.fill{position:absolute;inset:0;width:100%;height:100%}

/* cover layouts: positions in % of the slide so text never collides */
.cover-rule{position:absolute;left:3.6%;top:34.5%;width:1.1em;height:.1em;background:var(--blue)}
.cover-title{position:absolute;left:3.6%;top:37%;font-family:"Varela Round",sans-serif;font-size:.8em;line-height:1.15;color:var(--blue);white-space:nowrap}
.cover-sub{position:absolute;left:3.6%;top:57%;font-size:.52em;line-height:1.2;color:var(--white);white-space:nowrap}
.cover-mark{position:absolute;left:3.6%;bottom:6%;font-family:"Varela Round",sans-serif;font-size:.55em;color:var(--white)}
.on-blue .cover-title{color:var(--white)}
.on-blue .cover-rule{background:var(--white)}

.band-photo{left:0;top:0;right:0;bottom:22%}
.band-foot{position:absolute;left:0;right:0;bottom:0;height:22%;background:var(--white)}
.band-title{position:absolute;left:11%;bottom:9.5%;font-family:"Varela Round",sans-serif;font-size:.7em;line-height:1;color:var(--blue);white-space:nowrap}
.band-sub{position:absolute;left:11%;bottom:2.5%;font-size:.5em;line-height:1;color:var(--dim);white-space:nowrap}
.band-mark{position:absolute;right:4%;bottom:7%;font-family:"Varela Round",sans-serif;font-size:.55em;color:var(--dim)}
.band-notch{position:absolute;left:11%;top:78%;width:0;height:0;border-left:.3em solid transparent;border-right:.3em solid transparent;border-top:.4em solid var(--pink)}

.notch{position:absolute;width:0;height:0;border-left:3px solid transparent;border-right:3px solid transparent;border-top:4px solid var(--pink)}
.hd{position:absolute;left:10px;top:6px;font-family:"Varela Round",sans-serif;font-size:7.2px;color:var(--blue)}
.hd-rule{position:absolute;left:0;right:0;top:19px;height:.5px;background:var(--pink)}
.hd-rule .notch{left:14px;top:0;border-top-width:3px;border-left-width:2.5px;border-right-width:2.5px}
.ft{position:absolute;left:10px;bottom:4px;font-family:"Varela Round",sans-serif;font-size:3.6px;color:var(--dim)}
.pg{position:absolute;right:8px;bottom:5px;font-size:2.4px;color:var(--dim)}
.txt{font-size:3.5px;line-height:1.35;color:var(--dim)}
.tiny{font-size:2.3px;line-height:1.35;color:var(--dim)}
.lead{font-size:4.2px;font-weight:600;color:var(--dim);margin-bottom:1.5px}
.bul{position:relative;padding-left:5px;margin-bottom:1.5px}
.bul::before{content:"";position:absolute;left:1px;top:1.2px;width:1.4px;height:1.4px;border-radius:50%;background:var(--blue)}
.sub{position:relative;padding-left:13px;margin-bottom:1.5px;font-size:3px}
.sub::before{content:"–";position:absolute;left:7px;color:var(--blue)}
.toc{position:absolute;list-style:none}
.toc li{border-bottom:.5px solid var(--pink);font-size:3.6px;height:13.5px;line-height:13.5px;color:var(--dim);position:relative}
.toc li:first-child{border-top:.5px solid var(--pink)}
.toc b{font-weight:600;font-size:4.2px;color:var(--gray);margin-right:2px}
.toc li .notch{left:2px;top:0;border-top-width:2px;border-left-width:1.5px;border-right-width:1.5px}
.row{position:absolute;left:10px;right:10px;height:10px;display:flex;align-items:center;font-size:2.5px;color:var(--dim)}
.row .ic{width:10px;height:10px;display:flex;align-items:center;justify-content:center}
.row-blue{background:var(--ice)}
.row-pink{background:var(--pink)}
.quote-box{position:absolute;background:var(--blue);border-radius:3px;color:var(--white);font-size:3px;font-style:italic;text-align:center;padding:3px}
.service{position:absolute;left:0;right:0;top:28px;height:72px;background:var(--ice);display:flex;justify-content:space-around;padding:4px 6px}
.svc{width:42px;text-align:center}
.svc h4{font-size:2.8px;font-weight:600;margin:2px 0 1px;color:var(--dim)}
.chart-hd{position:absolute;font-size:4.5px;color:var(--dim)}
.legend{position:absolute;font-size:2.4px;color:var(--gray)}
.legend i{display:inline-block;width:2px;height:2px;margin:0 1px 0 3px}
.tbl{position:absolute;left:10px;right:10px;top:26px;border-collapse:collapse;font-size:2.1px;color:var(--dim)}
.tbl th{font-weight:600;font-size:2.6px;padding:1.5px 0}
.tbl thead tr:first-child th{background:var(--blue);color:var(--white)}
.tbl td{border-top:.4px solid var(--pink);padding:1.6px 2px;vertical-align:top;height:10px}
.qcard{position:absolute;top:28px;width:78px;height:45px;border:.6px solid var(--pink);padding:4px 5px;text-align:center}
.qmark{position:absolute;font-family:"Varela Round",sans-serif;font-size:8px;color:var(--blue);line-height:1}
.avatar{position:absolute;width:16px;height:16px;border-radius:50%;background:linear-gradient(135deg,#c9b9ab,#7c7670)}
.q-name{position:absolute;font-size:2.6px;color:var(--blue);text-align:center;width:60px}
.q-role{display:block;color:var(--dim);font-size:2.3px}
.tl-note{position:absolute;width:44px;font-size:2.2px;line-height:1.3;color:var(--dim)}
.ty-title{position:absolute;left:8px;top:20px;font-family:"Varela Round",sans-serif;font-size:8px;color:var(--blue)}
.ty-text{position:absolute;left:8px;top:38px;width:80px;font-size:2.6px;line-height:1.35;color:var(--white)}
.ty-contact{position:absolute;left:8px;font-size:2.6px;color:var(--white);display:flex;align-items:center;gap:4px}
</style>
</head>
<body>

<svg class="band" width="684" height="300" viewBox="0 0 684 300" aria-hidden="true">
  <path d="M0 0H684V188C560 250 300 262 0 196Z" fill="var(--dim)"/>
</svg>
<div class="brand">brennig-tautz</div>

<!-- hero: cover with photo band -->
<div class="hero hero-left">
  <section class="slide slide-cover-band">
    <div class="photo ph-stairs band-photo" role="img" aria-label="Photo of the coach smiling, seated on outdoor stone steps"></div>
    <div class="band-foot"></div>
    <div class="band-notch"></div>
    <div class="band-title">Presentation Title Here</div>
    <div class="band-sub">Sub Heading Title</div>
    <div class="band-mark">brennig-tautz</div>
  </section>
</div>

<!-- hero: cover with gray arc -->
<div class="hero hero-right">
  <section class="slide slide-cover-gray">
    <div class="photo ph-warm" style="left:40%;top:0;right:0;bottom:0" role="img" aria-label="Photo of the coach in an orange blazer seated on steps"></div>
    <svg class="fill" viewBox="0 0 205 115" preserveAspectRatio="none" aria-hidden="true"><path d="M0 0H145C103 32 98 86 124 115H0Z" fill="var(--dim)"/></svg>
    <div class="cover-rule"></div>
    <div class="cover-title">Presentation<br>Title Here</div>
    <div class="cover-sub">Sub Heading Title</div>
    <div class="cover-mark">brennig-tautz</div>
  </section>
</div>

<main class="deck">

  <!-- 1 cover gray -->
  <section class="slide slide-cover-gray">
    <div class="photo ph-warm" style="left:40%;top:0;right:0;bottom:0" role="img" aria-label="Photo of the coach in an orange blazer seated on steps"></div>
    <svg class="fill" viewBox="0 0 205 115" preserveAspectRatio="none" aria-hidden="true"><path d="M0 0H145C103 32 98 86 124 115H0Z" fill="var(--dim)"/></svg>
    <div class="cover-rule"></div>
    <div class="cover-title">Presentation<br>Title Here</div>
    <div class="cover-sub">Sub Heading Title</div>
    <div class="cover-mark">brennig-tautz</div>
  </section>

  <!-- 2 cover blue -->
  <section class="slide slide-cover-blue on-blue">
    <div class="photo ph-mono" style="left:40%;top:0;right:0;bottom:0" role="img" aria-label="Black and white portrait photo of the coach"></div>
    <svg class="fill" viewBox="0 0 205 115" preserveAspectRatio="none" aria-hidden="true"><path d="M0 0H82C120 22 122 88 95 115H0Z" fill="var(--blue)"/></svg>
    <div class="cover-rule"></div>
    <div class="cover-title">Presentation<br>Title Here</div>
    <div class="cover-sub">Sub Heading Title</div>
    <div class="cover-mark">brennig-tautz</div>
  </section>

  <!-- 3 cover band -->
  <section class="slide slide-cover-band">
    <div class="photo ph-stairs band-photo" role="img" aria-label="Photo of the coach smiling, seated on outdoor stone steps"></div>
    <div class="band-foot"></div>
    <div class="band-notch"></div>
    <div class="band-title">Presentation Title Here</div>
    <div class="band-sub">Sub Heading Title</div>
    <div class="band-mark">brennig-tautz</div>
  </section>

  <!-- 4 table of content -->
  <section class="slide">
    <div class="hd">Table of Content</div>
    <div class="hd-rule"><span class="notch"></span></div>
    <div class="photo ph-soft" style="left:0;top:26px;width:72px;height:72px" role="img" aria-label="Photo of the coach walking up stairs with a child"></div>
    <ul class="toc" style="left:84px;top:31px;width:108px">
      <li><b>01</b>Lorem ipsum dolor sit amet</li>
      <li><b>02</b>Lorem ipsum dolor sit amet</li>
      <li><b>03</b>Lorem ipsum dolor sit amet</li>
      <li><b>04</b>Lorem ipsum dolor sit amet</li>
      <li><b>05</b>Lorem ipsum dolor sit amet</li>
    </ul>
    <div class="ft">brennig-tautz</div><div class="pg">4</div>
  </section>

  <!-- 5 table of content dark -->
  <section class="slide">
    <div class="photo" style="left:0;top:0;width:88px;height:115px;background:linear-gradient(160deg,#5e5e5e,#4a4948)" role="img" aria-label="Dimmed photo of the coach walking with a child"></div>
    <div style="position:absolute;left:14px;top:42px;font-family:'Varela Round',sans-serif;font-size:6.4px;color:var(--blue)">Table of Content</div>
    <div style="position:absolute;left:14px;top:52px;width:62px;height:.5px;background:var(--pink)"></div>
    <div class="notch" style="left:18px;top:52px;border-top-width:3px"></div>
    <ul class="toc" style="left:98px;top:24px;width:96px">
      <li><span class="notch"></span><b>01</b>Lorem ipsum dolor sit amet</li>
      <li><span class="notch"></span><b>02</b>Lorem ipsum dolor sit amet</li>
      <li><span class="notch"></span><b>03</b>Lorem ipsum dolor sit amet</li>
      <li><span class="notch"></span><b>04</b>Lorem ipsum dolor sit amet</li>
      <li><span class="notch"></span><b>05</b>Lorem ipsum dolor sit amet</li>
    </ul>
    <div class="ft" style="color:var(--white)">brennig-tautz</div><div class="pg">5</div>
  </section>

  <!-- 6 icon rows -->
  <section class="slide">
    <div class="hd">Presentation Title Here</div>
    <div class="hd-rule"><span class="notch"></span></div>
    <div style="position:absolute;left:10px;top:23px">
      <div class="lead">Lorem Ipsum</div>
      <div class="tiny" style="font-size:2.8px">Sint brute at usu. Duo iisque appareat adversarium at.</div>
    </div>
    <div class="row row-blue" style="top:38px"><span class="ic"><svg width="5" height="5" viewBox="0 0 10 10"><rect x="2" y="1" width="6" height="8" rx="1" fill="none" stroke="var(--gray)" stroke-width=".8"/></svg></span>Lorem ipsum dolor sit amet, te ullum corpora delicata duo. Rebum insolens pri eu. No alia tota modus qui.</div>
    <div class="row row-pink" style="top:53px"><span class="ic"><svg width="5" height="5" viewBox="0 0 10 10"><circle cx="5" cy="4.5" r="3.5" fill="none" stroke="var(--gray)" stroke-width=".8"/></svg></span>Lorem ipsum dolor sit amet, te ullum corpora delicata duo. Rebum insolens pri eu. No alia tota modus qui.</div>
    <div class="row row-blue" style="top:68px"><span class="ic"><svg width="6" height="5" viewBox="0 0 12 10"><circle cx="4" cy="5" r="3" fill="none" stroke="var(--gray)" stroke-width=".8"/><circle cx="9" cy="5" r="2.2" fill="none" stroke="var(--gray)" stroke-width=".8"/></svg></span>Lorem ipsum dolor sit amet, te ullum corpora delicata duo. Rebum insolens pri eu. No alia tota modus qui.</div>
    <div class="row row-pink" style="top:83px"><span class="ic"><svg width="5" height="5" viewBox="0 0 10 10"><g fill="none" stroke="var(--gray)" stroke-width=".8"><circle cx="5" cy="5" r="1.5"/><circle cx="2" cy="2" r="1"/><circle cx="8" cy="2" r="1"/><circle cx="2" cy="8" r="1"/><circle cx="8" cy="8" r="1"/></g></svg></span>Lorem ipsum dolor sit amet, te ullum corpora delicata duo. Rebum insolens pri eu. No alia tota modus qui.</div>
    <div class="ft">brennig-tautz</div><div class="pg">6</div>
  </section>

  <!-- 7 two column -->
  <section class="slide">
    <div class="hd">Two Column</div>
    <div class="hd-rule"><span class="notch"></span></div>
    <div class="txt" style="position:absolute;left:10px;top:26px;width:88px">
      <div class="lead">Lorem Ipsum</div>
      <div class="bul">Lorem ipsum dolor sit amet, te ullum corpora delicata duo. Rebum insolens pri eu. No alia tota modus qui.</div>
      <div class="sub">Sint brute at usu. Duo iisque appareat adversarium at.</div>
      <div class="bul">Lorem ipsum dolor sit amet, te ullum corpora delicata duo. Rebum insolens pri eu. No alia tota modus qui.</div>
      <div class="sub">Sint brute at usu. Duo iisque appareat adversarium at.</div>
    </div>
    <div class="txt" style="position:absolute;left:106px;top:26px;width:88px">
      <div class="lead">Lorem Ipsum</div>
      <div class="bul">Lorem ipsum dolor sit amet, te ullum corpora delicata duo. Rebum insolens pri eu. No alia tota modus qui.</div>
      <div class="sub">Sint brute at usu. Duo iisque appareat adversarium at.</div>
      <div class="bul">Lorem ipsum dolor sit amet, te ullum corpora delicata duo. Rebum insolens pri eu. No alia tota modus qui.</div>
      <div class="sub">Sint brute at usu. Duo iisque appareat adversarium at.</div>
    </div>
    <div class="ft">brennig-tautz</div><div class="pg">7</div>
  </section>

  <!-- 8 left column -->
  <section class="slide">
    <div class="hd">Left Column</div>
    <div class="hd-rule" style="right:95px"><span class="notch"></span></div>
    <div class="photo ph-desk" style="left:112px;top:0;right:0;bottom:0" role="img" aria-label="Photo of hands working on a tablet at a desk"></div>
    <div class="txt" style="position:absolute;left:10px;top:26px;width:90px">
      <div class="lead">Lorem Ipsum</div>
      <div class="bul">Lorem ipsum dolor sit amet, te ullum corpora delicata duo. Rebum insolens pri eu. No alia tota modus qui.</div>
      <div class="sub">Sint brute at usu. Duo iisque appareat adversarium at.</div>
      <div class="bul">Lorem ipsum dolor sit amet, te ullum corpora delicata duo. Rebum insolens pri eu. No alia tota modus qui.</div>
      <div class="sub">Sint brute at usu. Duo iisque appareat adversarium at.</div>
    </div>
    <div class="ft">brennig-tautz</div><div class="pg">8</div>
  </section>

  <!-- 9 about us -->
  <section class="slide">
    <div class="hd">About Us</div>
    <div class="hd-rule"><span class="notch"></span></div>
    <div class="photo ph-soft" style="left:0;top:24px;width:77px;bottom:0" role="img" aria-label="Portrait photo of the coach resting her chin on her hand"></div>
    <div class="quote-box" style="left:15px;top:73px;width:58px">“Lorem ipsum dolor sit amet, te ullum corpora delicata duo”</div>
    <div class="txt" style="position:absolute;left:93px;top:26px;width:88px">
      <p style="margin-bottom:2px">Lorem ipsum dolor sit amet, te ullum corpora delicata duo. Rebum insolens pri eu. No alia tota modus qui. Lorem ipsum dolor sit amet, te ullum corpora delicata duo. Rebum insolens pri eu. No alia tota modus qui. Lorem ipsum dolor sit amet, te ullum corpora delicata duo. Rebum insolens pri eu. No alia tota modus qui.</p>
      <p>Lorem ipsum dolor sit amet, te ullum corpora delicata duo. Rebum insolens pri eu. No alia tota modus qui.</p>
    </div>
    <div style="position:absolute;left:166px;top:96px;font-size:3.4px;font-weight:600;color:var(--dim)">Your <span style="color:var(--blue)">Name</span><span class="q-role" style="font-weight:400">Your Title Job</span></div>
    <div class="ft" style="color:var(--white)">brennig-tautz</div><div class="pg">9</div>
  </section>

  <!-- 10 service -->
  <section class="slide">
    <div class="hd">Service &amp; Kooperation</div>
    <div class="hd-rule"><span class="notch"></span></div>
    <div class="service">
      <div class="svc"><svg width="22" height="22" viewBox="0 0 22 22"><circle cx="11" cy="11" r="10" fill="var(--white)" stroke="var(--blue)" stroke-width=".8"/><rect x="7" y="6" width="6" height="10" rx="1" fill="none" stroke="var(--gray)" stroke-width=".6"/><rect x="11" y="9" width="5" height="7" rx=".8" fill="none" stroke="var(--gray)" stroke-width=".6"/></svg><h4>#Digital first</h4><div class="tiny">Coachings, Workshops und Trainings bieten wir klassisch und online an. Konzepte ab dem ersten Tag.</div></div>
      <div class="svc"><svg width="22" height="22" viewBox="0 0 22 22"><circle cx="11" cy="11" r="10" fill="var(--white)" stroke="var(--blue)" stroke-width=".8"/><circle cx="11" cy="10" r="5" fill="none" stroke="var(--gray)" stroke-width=".6"/><path d="M6 10h10M11 5v10M8 17h6" stroke="var(--gray)" stroke-width=".5"/></svg><h4>#International</h4><div class="tiny">Je nach Thema moderieren wir Workshops auch in Englisch. Teams können global verteilt sein.</div></div>
      <div class="svc"><svg width="22" height="22" viewBox="0 0 22 22"><circle cx="11" cy="11" r="10" fill="var(--white)" stroke="var(--blue)" stroke-width=".8"/><circle cx="8.5" cy="11" r="2.6" fill="none" stroke="var(--gray)" stroke-width=".6"/><circle cx="14" cy="10" r="2" fill="none" stroke="var(--gray)" stroke-width=".6"/></svg><h4>#Customized</h4><div class="tiny">Meine Formate sind auf die Bedürfnisse der Kunden angepasst und entstehen im iterativen Prozess.</div></div>
      <div class="svc"><svg width="22" height="22" viewBox="0 0 22 22"><circle cx="11" cy="11" r="10" fill="var(--white)" stroke="var(--blue)" stroke-width=".8"/><g fill="none" stroke="var(--gray)" stroke-width=".6"><circle cx="11" cy="11" r="1.8"/><circle cx="6.5" cy="7" r="1.2"/><circle cx="15.5" cy="7" r="1.2"/><circle cx="6.5" cy="15" r="1.2"/><circle cx="15.5" cy="15" r="1.2"/><path d="M7.4 7.8l2.3 2M14.6 7.8l-2.3 2M7.4 14.2l2.3-2M14.6 14.2l-2.3-2"/></g></svg><h4>#Networks</h4><div class="tiny">Alleine bin ich stark, im Netzwerk noch stärker. Für umfangreiche Projekte arbeite ich mit Partnern.</div></div>
    </div>
    <div class="ft">brennig-tautz</div><div class="pg">10</div>
  </section>

  <!-- 11 bar chart -->
  <section class="slide">
    <div class="hd">Bar Chart Sample</div>
    <div class="hd-rule"><span class="notch"></span></div>
    <div class="chart-hd" style="left:42px;top:24px">Heading Here</div>
    <svg style="position:absolute;left:8px;top:32px" width="95" height="65" viewBox="0 0 95 65" aria-label="Bar chart with three series across four categories">
      <g font-size="2.6" fill="var(--gray)" font-family="Montserrat,sans-serif">
        <text x="0" y="6">6</text><text x="0" y="15">5</text><text x="0" y="24">4</text><text x="0" y="33">3</text><text x="0" y="42">2</text><text x="0" y="51">1</text><text x="0" y="60">0</text>
        <text x="13" y="64">Category 1</text><text x="34" y="64">Category 2</text><text x="55" y="64">Category 3</text><text x="76" y="64">Category 4</text>
      </g>
      <g>
        <rect x="9" y="19" width="5" height="40" fill="var(--dim)"/><rect x="15" y="37" width="5" height="22" fill="var(--blue)"/><rect x="21" y="41" width="5" height="18" fill="var(--gray)"/>
        <rect x="30" y="36" width="5" height="23" fill="var(--dim)"/><rect x="36" y="19" width="5" height="40" fill="var(--blue)"/><rect x="42" y="41" width="5" height="18" fill="var(--gray)"/>
        <rect x="51" y="28" width="5" height="31" fill="var(--dim)"/><rect x="57" y="41" width="5" height="18" fill="var(--blue)"/><rect x="63" y="32" width="5" height="27" fill="var(--gray)"/>
        <rect x="72" y="19" width="5" height="40" fill="var(--dim)"/><rect x="78" y="34" width="5" height="25" fill="var(--blue)"/><rect x="84" y="14" width="5" height="45" fill="var(--gray)"/>
      </g>
    </svg>
    <div class="legend" style="left:30px;top:99px"><i style="background:var(--dim)"></i>Series 1<i style="background:var(--blue)"></i>Series 2<i style="background:var(--gray)"></i>Series 3</div>
    <div class="txt" style="position:absolute;left:112px;top:26px;width:84px">
      <div class="lead">Lorem Ipsum</div>
      <div class="bul">Lorem ipsum dolor sit amet, te ullum corpora delicata duo. Rebum insolens pri eu. No alia tota modus qui.</div>
      <div class="sub">Sint brute at usu. Duo iisque appareat adversarium at.</div>
      <div class="bul">Lorem ipsum dolor sit amet, te ullum corpora delicata duo. Rebum insolens pri eu. No alia tota modus qui.</div>
    </div>
    <div class="ft">brennig-tautz</div><div class="pg">11</div>
  </section>

  <!-- 12 horizontal bar chart -->
  <section class="slide">
    <div class="hd">Bar Chart Sample</div>
    <div class="hd-rule"><span class="notch"></span></div>
    <div class="chart-hd" style="left:42px;top:24px">Heading Here</div>
    <svg style="position:absolute;left:8px;top:32px" width="100" height="65" viewBox="0 0 100 65" aria-label="Horizontal bar chart with three series across four categories">
      <g font-size="2.6" fill="var(--gray)" font-family="Montserrat,sans-serif">
        <text x="0" y="8">Category 4</text><text x="0" y="22">Category 3</text><text x="0" y="36">Category 2</text><text x="0" y="50">Category 1</text>
        <text x="28" y="62">0</text><text x="40" y="62">1</text><text x="52" y="62">2</text><text x="64" y="62">3</text><text x="76" y="62">4</text><text x="88" y="62">5</text>
      </g>
      <rect x="29" y="1" width="56" height="3.5" fill="var(--dim)"/><rect x="29" y="5" width="33" height="3.5" fill="var(--blue)"/><rect x="29" y="9" width="53" height="3.5" fill="var(--gray)"/>
      <rect x="29" y="15" width="22" height="3.5" fill="var(--dim)"/><rect x="29" y="19" width="21" height="3.5" fill="var(--blue)"/><rect x="29" y="23" width="42" height="3.5" fill="var(--gray)"/>
      <rect x="29" y="29" width="24" height="3.5" fill="var(--dim)"/><rect x="29" y="33" width="53" height="3.5" fill="var(--blue)"/><rect x="29" y="37" width="30" height="3.5" fill="var(--gray)"/>
      <rect x="29" y="43" width="24" height="3.5" fill="var(--dim)"/><rect x="29" y="47" width="29" height="3.5" fill="var(--blue)"/><rect x="29" y="51" width="52" height="3.5" fill="var(--gray)"/>
    </svg>
    <div class="legend" style="left:34px;top:99px"><i style="background:var(--gray)"></i>Series 3<i style="background:var(--blue)"></i>Series 2<i style="background:var(--dim)"></i>Series 1</div>
    <div class="txt" style="position:absolute;left:112px;top:26px;width:84px">
      <div class="lead">Lorem Ipsum</div>
      <div class="bul">Lorem ipsum dolor sit amet, te ullum corpora delicata duo. Rebum insolens pri eu. No alia tota modus qui.</div>
      <div class="sub">Sint brute at usu. Duo iisque appareat adversarium at.</div>
      <div class="bul">Lorem ipsum dolor sit amet, te ullum corpora delicata duo. Rebum insolens pri eu. No alia tota modus qui.</div>
    </div>
    <div class="ft">brennig-tautz</div><div class="pg">12</div>
  </section>

  <!-- 13 pie chart -->
  <section class="slide">
    <div class="hd">Pie Chart Sample</div>
    <div class="hd-rule"><span class="notch"></span></div>
    <div class="chart-hd" style="left:43px;top:24px">Heading Here</div>
    <svg style="position:absolute;left:0;top:0" width="110" height="115" viewBox="0 0 110 115" aria-label="Pie chart with four categories">
      <path d="M60 60L60 31A29 29 0 0 1 88.1 67.3Z" fill="var(--dim)"/>
      <path d="M60 60L88.1 67.3A29 29 0 0 1 67.3 88.1Z" fill="var(--blue)"/>
      <path d="M60 60L67.3 88.1A29 29 0 0 1 32.6 69.7Z" fill="var(--gray)"/>
      <path d="M60 60L32.6 69.7A29 29 0 0 1 60 31Z" fill="var(--pink)"/>
      <g font-size="5" fill="var(--white)" font-family="Montserrat,sans-serif">
        <text x="68" y="52">4,3</text><text x="70" y="74">2,5</text><text x="49" y="77">3,5</text><text x="42" y="55" fill="var(--dim)">4,5</text>
      </g>
    </svg>
    <div class="legend" style="left:18px;top:97px"><i style="background:var(--dim)"></i>Category 1<i style="background:var(--blue)"></i>Category 2<i style="background:var(--gray)"></i>Category 3<i style="background:var(--pink)"></i>Category 4</div>
    <div class="txt" style="position:absolute;left:112px;top:26px;width:84px">
      <div class="lead">Lorem Ipsum</div>
      <div class="bul">Lorem ipsum dolor sit amet, te ullum corpora delicata duo. Rebum insolens pri eu. No alia tota modus qui.</div>
      <div class="sub">Sint brute at usu. Duo iisque appareat adversarium at.</div>
      <div class="bul">Lorem ipsum dolor sit amet, te ullum corpora delicata duo. Rebum insolens pri eu. No alia tota modus qui.</div>
    </div>
    <div class="ft">brennig-tautz</div><div class="pg">13</div>
  </section>

  <!-- 14 donut chart -->
  <section class="slide">
    <div class="hd">Donat Chart Sample</div>
    <div class="hd-rule"><span class="notch"></span></div>
    <div class="chart-hd" style="left:43px;top:24px">Heading Here</div>
    <svg style="position:absolute;left:0;top:0" width="110" height="115" viewBox="0 0 110 115" aria-label="Donut chart with four categories">
      <g transform="rotate(-90 60 60)" fill="none" stroke-width="13">
        <circle cx="60" cy="60" r="20" stroke="var(--dim)" stroke-dasharray="36.4 125.7"/>
        <circle cx="60" cy="60" r="20" stroke="var(--blue)" stroke-dasharray="21.4 125.7" stroke-dashoffset="-36.4"/>
        <circle cx="60" cy="60" r="20" stroke="var(--gray)" stroke-dasharray="30.2 125.7" stroke-dashoffset="-57.8"/>
        <circle cx="60" cy="60" r="20" stroke="var(--pink)" stroke-dasharray="37.7 125.7" stroke-dashoffset="-88"/>
      </g>
      <g font-size="3.2" fill="var(--white)" font-family="Montserrat,sans-serif">
        <text x="71" y="51">29%</text><text x="71" y="72">17%</text><text x="51" y="81">24%</text><text x="42" y="52" fill="var(--dim)">30%</text>
      </g>
    </svg>
    <div class="legend" style="left:18px;top:97px"><i style="background:var(--dim)"></i>Category 1<i style="background:var(--blue)"></i>Category 2<i style="background:var(--gray)"></i>Category 3<i style="background:var(--pink)"></i>Category 4</div>
    <div class="txt" style="position:absolute;left:112px;top:26px;width:84px">
      <div class="lead">Lorem Ipsum</div>
      <div class="bul">Lorem ipsum dolor sit amet, te ullum corpora delicata duo. Rebum insolens pri eu. No alia tota modus qui.</div>
      <div class="sub">Sint brute at usu. Duo iisque appareat adversarium at.</div>
      <div class="bul">Lorem ipsum dolor sit amet, te ullum corpora delicata duo. Rebum insolens pri eu. No alia tota modus qui.</div>
    </div>
    <div class="ft">brennig-tautz</div><div class="pg">14</div>
  </section>

  <!-- 15 table -->
  <section class="slide">
    <div class="hd">Table Sample</div>
    <div class="hd-rule"><span class="notch"></span></div>
    <table class="tbl">
      <thead>
        <tr><th colspan="4">LOREM IPSUM</th></tr>
        <tr><th>Lorem ipsum</th><th>Lorem ipsum 1</th><th>Lorem ipsum 2</th><th>Lorem ipsum 3</th></tr>
      </thead>
      <tbody>
        <tr><td>• Lorem ipsum dolor sit amet, consectetur adipiscing elit.</td><td>• Lorem ipsum dolor sit amet, consectetur adipiscing elit.</td><td>• Lorem ipsum dolor sit amet, consectetur adipiscing elit.</td><td>• Lorem ipsum dolor sit amet, consectetur adipiscing elit.</td></tr>
        <tr><td>• Lorem ipsum dolor sit amet, consectetur adipiscing elit.</td><td>• Lorem ipsum dolor sit amet, consectetur adipiscing elit.</td><td>• Quisque nec enim luctus, finibus leo vulputate.</td><td>• Quisque nec enim luctus, finibus leo vulputate.</td></tr>
        <tr><td>• Lorem ipsum dolor sit amet, consectetur adipiscing elit.</td><td>• Lorem ipsum dolor sit amet, consectetur adipiscing elit.</td><td>• Lorem ipsum dolor sit amet, consectetur adipiscing elit.</td><td>• Lorem ipsum dolor sit amet, consectetur adipiscing elit.</td></tr>
        <tr><td>• Lorem ipsum dolor sit amet.</td><td>• Lorem ipsum dolor sit amet.</td><td>• Lorem ipsum dolor sit amet.</td><td>• Lorem ipsum dolor sit amet.</td></tr>
      </tbody>
    </table>
    <div class="ft">brennig-tautz</div><div class="pg">15</div>
  </section>

  <!-- 16 quotes -->
  <section class="slide">
    <div class="hd">Quote Sample</div>
    <div class="hd-rule"><span class="notch"></span></div>
    <div class="qcard tiny" style="left:13px">In both the conceptualization and the execution of our Leadership Program at ordwise, she was a valuable source of support. With dedication, flexibility and passion for people she ran a remote training program for Managers even in times of unprecedented challenges.</div>
    <span class="qmark" style="left:9px;top:25px">“</span><span class="qmark" style="left:86px;top:67px">”</span>
    <div class="qcard tiny" style="left:113px">Ich habe die Zusammenarbeit immer sehr geschätzt. Sie verliert das Wesentliche nie aus den Augen und kann mit Komplexität umgehen. Sie arbeitet professionell und in top Qualität mit viel Feingefühl und Empathie.</div>
    <span class="qmark" style="left:109px;top:25px">“</span><span class="qmark" style="left:186px;top:67px">”</span>
    <div class="avatar" style="left:83px;top:75px" role="img" aria-label="Portrait photo of the first reference"></div>
    <div class="avatar" style="left:177px;top:75px" role="img" aria-label="Portrait photo of the second reference"></div>
    <div class="q-name" style="left:62px;top:93px">Jonas Ferrant<span class="q-role">Global Director Talent &amp; Culture, ordwise</span></div>
    <div class="q-name" style="left:150px;top:93px">Lena Vostrik<span class="q-role">COO Halden Retail Lab</span></div>
    <div class="ft">brennig-tautz</div><div class="pg">16</div>
  </section>

  <!-- 17 timeline -->
  <section class="slide">
    <div class="hd">Timeline Sample</div>
    <div class="hd-rule"><span class="notch"></span></div>
    <svg style="position:absolute;left:0;top:0" width="205" height="115" viewBox="0 0 205 115" aria-label="Timeline with six steps">
      <g fill="var(--ice)">
        <path d="M9 52H38L42 60L38 68H9Z"/>
        <path d="M41 52H68L72 60L68 68H41L45 60Z" fill="var(--pink)"/>
        <path d="M71 52H98L102 60L98 68H71L75 60Z"/>
        <path d="M101 52H128L132 60L128 68H101L105 60Z" fill="var(--pink)"/>
        <path d="M131 52H158L162 60L158 68H131L135 60Z"/>
        <path d="M161 52H188L192 60L188 68H161L165 60Z" fill="var(--pink)"/>
      </g>
      <g font-family="Montserrat,sans-serif" fill="var(--dim)">
        <g font-size="3" font-weight="600"><text x="12" y="57">TEXT 1</text><text x="46" y="57">TEXT 2</text><text x="76" y="57">TEXT 3</text><text x="106" y="57">TEXT 4</text><text x="136" y="57">TEXT 5</text><text x="166" y="57">TEXT 6</text></g>
        <g font-size="2.2"><text x="12" y="62">Lorem ipsum</text><text x="46" y="62">Lorem ipsum</text><text x="76" y="62">Lorem ipsum</text><text x="106" y="62">Lorem ipsum</text><text x="136" y="62">Lorem ipsum</text><text x="166" y="62">Lorem ipsum</text></g>
      </g>
      <g stroke="var(--gray)" stroke-width=".4">
        <path d="M25 52V38M85 52V38M145 52V38M55 68V82M115 68V82M175 68V82"/>
      </g>
    </svg>
    <div class="tl-note" style="left:13px;top:28px">Lorem ipsum dolor sit amet, te ullum corpora delicata duo.</div>
    <div class="tl-note" style="left:73px;top:28px">Lorem ipsum dolor sit amet, te ullum corpora delicata duo.</div>
    <div class="tl-note" style="left:133px;top:28px">Lorem ipsum dolor sit amet, te ullum corpora delicata duo.</div>
    <div class="tl-note" style="left:40px;top:85px">Lorem ipsum dolor sit amet, te ullum corpora delicata duo.</div>
    <div class="tl-note" style="left:100px;top:85px">Lorem ipsum dolor sit amet, te ullum corpora delicata duo.</div>
    <div class="tl-note" style="left:155px;top:85px">Lorem ipsum dolor sit amet, te ullum corpora delicata duo.</div>
    <div class="ft">brennig-tautz</div><div class="pg">17</div>
  </section>

  <!-- 18 thank you -->
  <section class="slide">
    <div class="photo ph-warm" style="left:90px;top:0;right:0;bottom:0" role="img" aria-label="Photo of the coach in an orange blazer seated on steps"></div>
    <svg class="fill" viewBox="0 0 205 115" preserveAspectRatio="none" aria-hidden="true"><path d="M0 0H145C103 32 98 86 124 115H0Z" fill="var(--dim)"/></svg>
    <div style="position:absolute;left:8px;top:18px;width:9px;height:.8px;background:var(--blue)"></div>
    <div class="ty-title">Thank You</div>
    <div class="ty-text">Lorem Ipsum is simply dummy text of the printing and typesetting industry. Lorem Ipsum has been the industry's standard dummy text ever since the 1500s, when an unknown printer took a galley of type and scrambled it.</div>
    <div class="ty-contact" style="top:62px"><svg width="4" height="3" viewBox="0 0 8 6"><rect width="8" height="6" fill="var(--white)"/><path d="M0 0L4 3.5L8 0" stroke="var(--dim)" stroke-width=".8" fill="none"/></svg>Lorem ipsum</div>
    <div class="ty-contact" style="top:72px"><svg width="4" height="4" viewBox="0 0 8 8"><circle cx="4" cy="4" r="3.5" fill="none" stroke="var(--white)" stroke-width="1"/></svg>Lorem ipsum</div>
    <div class="ty-contact" style="top:82px"><svg width="3" height="4" viewBox="0 0 6 8"><path d="M3 8C3 8 0 4.5 0 3A3 3 0 0 1 6 3C6 4.5 3 8 3 8Z" fill="var(--white)"/><circle cx="3" cy="3" r="1" fill="var(--dim)"/></svg>Lorem ipsum</div>
    <div class="cover-mark" style="left:8px;bottom:7px">brennig-tautz</div>
  </section>

</main>
</body>
</html>
```